Designing a website for Brightmoor Pest Services PTY LTD

Pest control company looking for someone to build an informative website containing services we offer and an online inquiry form.
Commercial premises - Specialising in - Rodent control, stored product pest control, flying insect control, ant, spider and insect control, Termite inspections and treatments. Termite management systems on a commercial scale.
Facilities we service
Commercial - shopping centres, transport facilities, restaurants, pubs, clubs, bars food manufacturing facilities.
Residential - Houses specialising in - Rodent, Ant, Spider, Cockroach and Termite control. Termite inspections, Pre - purchase inspections, Termite treatments, Termite management systems.
Target Market(s)
Mainly commercial and industrial clients and Residential clients.
Industry/Entity Type
Pest Control
Number of Pages Required
1 page
Look and feel

```html
<!DOCTYPE html>
<html lang="en">
<head>
<meta charset="utf-8">
<title>Brightmoor Pest Services</title>
<link rel="stylesheet" href="https://fonts.googleapis.com/css2?family=Bitter:wght@400;700&family=PT+Sans:wght@400;700&family=Open+Sans:wght@300;400&display=swap">
<style>
  :root {
    --page-dark: #2b2b2b;
    --strip-black: #0c0c0c;
    --band-light: #e6e6e6;
    --band-lighter: #f6f6f6;
    --brand-green: #5e9a24;
    --button-green: #bfe07a;
    --button-green-dark: #97c645;
    --text-dark: #222222;
    --text-grey: #555555;
    --text-white: #f2f2f2;
    --rule-grey: #6a6a6a;
  }
  * { margin: 0; padding: 0; box-sizing: border-box; }
  html, body { width: 1200px; height: 789px; overflow: hidden; }
  body { background: var(--page-dark); position: relative; font-family: "PT Sans", sans-serif; }

  .site-header { position: absolute; top: 0; left: 0; width: 1200px; height: 200px; }
  .brand { position: absolute; left: 150px; top: 118px; display: flex; align-items: center; gap: 12px; }
  .brand-dot { width: 20px; height: 20px; border-radius: 50%; background: var(--brand-green); }
  .brand-name { font-family: "PT Sans", sans-serif; font-weight: 700; font-size: 24px; color: var(--text-white); }

  .main-nav { position: absolute; top: 58px; left: 500px; display: flex; gap: 46px; }
  .main-nav a { font-family: "Bitter", serif; font-size: 14px; color: var(--text-white); text-decoration: none; position: relative; }
  .main-nav a.is-active { color: var(--brand-green); }
  .main-nav a.is-active::before { content: ""; position: absolute; left: -6px; right: -6px; top: -14px; height: 2px; background: var(--brand-green); }

  .hero-band { position: absolute; top: 190px; left: 0; width: 1200px; height: 300px;
    background: linear-gradient(90deg, var(--band-light), var(--band-lighter) 45%, var(--band-light)); }

  .hero-artwork { position: absolute; left: 700px; top: 165px; width: 420px; height: 400px; border-radius: 48% 30% 30% 48%;
    background: radial-gradient(ellipse at 62% 45%, #cfcfcf 0%, #9a9a9a 35%, #4f7a25 62%, rgba(94,154,36,0.55) 78%, rgba(43,43,43,0) 100%); }

  .hero-copy { position: absolute; left: 215px; top: 222px; width: 440px; }
  .hero-title { font-family: "Bitter", serif; font-weight: 700; font-size: 30px; line-height: 1.18; color: var(--text-dark); }
  .hero-lead { margin-top: 12px; font-weight: 700; font-size: 19px; line-height: 1.12; color: var(--brand-green); text-align: justify; }
  .hero-note { margin-top: 8px; font-size: 14px; color: var(--text-grey); }
  .hero-note strong { font-weight: 700; }
  .contact-button { margin-top: 16px; display: inline-flex; align-items: center; gap: 16px; width: 196px; height: 40px; padding: 0 14px;
    background: linear-gradient(180deg, var(--button-green), var(--button-green-dark)); border: 1px solid #a6d15a;
    font-family: "Open Sans", sans-serif; font-size: 11px; color: #3e5f14; text-transform: uppercase; text-decoration: none; }
  .contact-button .tick { width: 18px; height: 18px; border-radius: 50%; background: var(--brand-green); display: flex; align-items: center; justify-content: center; }

  .facilities { position: absolute; top: 560px; left: 0; width: 1200px; }
  .facilities-title { position: absolute; left: 320px; top: 28px; font-family: "Open Sans", sans-serif; font-weight: 300; font-size: 36px; color: var(--text-white); text-transform: uppercase; letter-spacing: 0.5px; }
  .facilities-rule { position: absolute; left: 320px; top: 82px; width: 820px; height: 2px; background: var(--rule-grey); }
  .facilities-photo { position: absolute; left: 240px; top: 120px; width: 960px; height: 110px;
    background: radial-gradient(ellipse at 30% 100%, #6b5520 0%, #1a160c 25%, var(--strip-black) 55%); }
</style>
</head>
<body>
  <header class="site-header">
    <div class="brand">
      <span class="brand-dot"></span>
      <span class="brand-name">Brightmoor Pest Services</span>
    </div>
    <nav class="main-nav">
      <a class="is-active" href="#">Home</a>
      <a href="#">Services</a>
      <a href="#">Comercial</a>
      <a href="#">Residencial</a>
      <a href="#">Conatct</a>
    </nav>
  </header>

  <section class="hero-band"></section>

  <div class="hero-artwork" role="img" aria-label="Green and black crescent swoosh framing silhouettes of a rat, spider, ants, cockroach and flies"></div>

  <div class="hero-copy">
    <h1 class="hero-title">The ultimate commercial pest control solution.</h1>
    <p class="hero-lead">We are experts in rodent control, stored product pest control, flying insect control, ant, spider and insect control, termite inspections and treatments.</p>
    <p class="hero-note">Termite management systems on a <strong>commerdal scale.</strong></p>
    <a class="contact-button" href="#">
      <span class="tick"><svg width="10" height="10" viewBox="0 0 10 10"><path d="M1.5,5 L4,7.5 L8.5,2.5" fill="none" stroke="#eaf5d4" stroke-width="1.6"/></svg></span>
      Contact now
    </a>
  </div>

  <section class="facilities">
    <h2 class="facilities-title">Service Facilities</h2>
    <div class="facilities-rule"></div>
    <div class="facilities-photo" role="img" aria-label="Night photograph of a lit commercial facility"></div>
  </section>
</body>
</html>
```